FenderPals Personal Injury Lawyers Website (Wordpress)

We need a brand new website for our firm's new rebranding. The name of the website is www.fenderpals-example.com. Our new brand will be a group of personal injury lawyers focused on representing only victims in car wrecks. We will be distinguishing ourselves from other law firms due to the fact that other law firms represent clients involving all forms of personal injury. We will only focus on car wrecks and this needs to be reflected on the website.

I have attached the new firm logo and stationary to show the designers the kind of look we are going for in the new website. It needs to be clean, pure, and show the potential clients that we only do one thing and we do it well. That thing is car wrecks.

Some examples of websites that we like are the following:
www.qvt-example.lu - nice interface and colors. nice navigation, we really like the biography pages for the individuals attorneys
www.morvantlegal-example.com - good layout, good navigation
www.pelliardwoss-example.com - navigation bar follows the user whether the user goes up or down

We would like five separate pages -- (1) Home, (2) Client Resources, (3) Expertise / Car Wrecks, (4) Contact Us, (5) News

The Home page will be used for driving traffic and should have a call to action on the right at the top stating that we will send an ebook to anyone who gives their contact information. The ebook will explain how car wrecks work. This should also have room for youtube videos which will be added later.

The client resources will include blogs, books, and information for potential clients. It should be presented in a well developed manner which is both appealing to potential and current clients.

The expertise page will show that we only focus on car wrecks. This needs to be a recurrent theme throughout the entire website. This page will focus on car wrecks and the different aspects including damages, insurance, and investigation.

The Contact Us page will show a google map to our address and phone number. Please use generic information and we will fill in the gaps upon the selection.

News: the news page will show different articles related to past and present cases and the successes of those clients.

The overall page should be elegant and creative. Do not include courthouses, gavels or anything else related to the law. If you include these things, your design will automatically be excluded.
Updates

Please take note this design is now guaranteed. I look forward to receiving everyone's wonderful designs.

Target Market(s)

Persons involved in car wrecks

Industry/Entity Type

Legal

Coding

Coded - Design and coding required

Number of Pages Required

5+ page

Font styles to use
Serif
Sans Serif

Colors
ec1f27
ffffff
000000

Requirements
Must have
• Five pages which focus on representation of car wreck victims. The site must be clean and easy to navigate.
Nice to have
• Navigation bar should follow user up and down the page.
Should not have
• Gavels, court houses, anything related to the law. If your design has these aspects, it will automatically be rejected

```html
<!DOCTYPE html>
<html lang="en">
<head>
<meta charset="utf-8">
<title>FenderPals – Personal Injury Lawyers</title>
<link href="https://fonts.googleapis.com/css2?family=Open+Sans:wght@400;600;700&display=swap" rel="stylesheet">
<style>
:root{
  --red:#ec1f27;
  --blue:#1c6cc0;
  --blue-dark:#15529a;
  --ink:#222;
  --muted:#6b6b6b;
  --line:#e2e2e2;
  --panel:#f0f0f0;
  --footer:#ebebeb;
  --footer-bar:#2b2b2b;
  --white:#fff;
}
*{box-sizing:border-box;margin:0;padding:0}
html,body{width:692px;height:1200px;overflow:hidden;background:var(--white)}
body{font-family:"Open Sans",Arial,sans-serif;color:var(--ink);font-size:7px;line-height:1.45}
.topbar{height:18px;display:flex;justify-content:space-between;align-items:center;padding:0 54px;font-size:6px;color:var(--muted);border-bottom:1px solid var(--line)}
.social{display:flex;gap:4px}
.social span{width:8px;height:8px;border-radius:50%;background:#999}
.header{height:42px;display:flex;align-items:center;justify-content:space-between;padding:0 54px}
.brand{font-size:20px;font-weight:700;color:var(--red);letter-spacing:.5px}
.nav{display:flex;align-items:center;gap:2px}
.nav a{font-size:6.5px;color:var(--ink);text-decoration:none;padding:4px 6px}
.nav a.active{background:var(--red);color:var(--white)}
.nav .badge{width:20px;height:20px;border-radius:50%;background:var(--red);margin-left:6px}
.hero{height:286px;background:linear-gradient(180deg,var(--blue),var(--blue-dark));padding:22px 54px 0;color:var(--white);position:relative}
.hero h1{text-align:center;font-size:17px;font-weight:600;margin-bottom:14px}
.hero-body{display:flex;gap:20px}
.hero-copy{width:300px}
.hero-copy p{font-size:6.2px;margin-bottom:10px;opacity:.92}
.checklist{background:var(--white);list-style:none;padding:6px 10px;color:var(--ink)}
.checklist li{display:flex;align-items:center;gap:6px;font-size:6.2px;padding:2.5px 0;border-bottom:1px solid #f1f1f1}
.checklist li:last-child{border:0}
.hero-photo{width:274px;height:152px;border:3px solid var(--white);background:linear-gradient(135deg,#9fb3c6,#2a4f9a 55%,#1f2a3a)}
.aspects{height:196px;padding-top:30px;text-align:center}
.aspects h2{font-size:15px;font-weight:600;line-height:1.3;color:#333}
.aspect-row{display:flex;justify-content:center;gap:58px;margin-top:30px;text-align:left}
.aspect{display:flex;gap:10px;width:140px}
.aspect svg{flex:none}
.aspect h3{font-size:8px;font-weight:600;margin-bottom:2px}
.aspect p{font-size:6.2px;color:var(--muted)}
.cta{margin:10px 54px 0;height:100px;background:var(--panel);border:1px solid var(--line);text-align:center;padding-top:14px}
.cta h2{font-size:14px;font-weight:600;color:#333;margin-bottom:5px}
.cta p{font-size:6px;color:var(--muted);width:460px;margin:0 auto}
.btn{display:inline-block;margin-top:9px;background:var(--red);color:var(--white);font-size:6px;padding:3px 10px}
.reviews{height:326px;text-align:center;padding-top:32px}
.reviews h2{font-size:16px;font-weight:600;color:#333}
.reviews .intro{font-size:6.2px;color:var(--muted);width:340px;margin:6px auto 0}
.review-row{display:flex;justify-content:center;gap:110px;margin-top:18px}
.review{width:110px}
.avatar{width:88px;height:88px;border-radius:50%;margin:0 auto;border:4px solid #f2f2f2;background:radial-gradient(circle at 50% 40%,#c9c9c9,#5f6a78)}
.review p{font-size:6px;color:var(--muted);margin-top:10px;text-align:left}
.review cite{display:block;font-size:6px;font-style:italic;margin-top:6px;text-align:left}
.footer{position:absolute;top:982px;left:0;width:692px;height:194px;background:var(--footer);display:flex;gap:0;padding:30px 54px 0}
.col{width:146px}
.col h4{font-size:9px;font-weight:600;color:#333;margin-bottom:6px}
.col li{list-style:none;font-size:5.8px;color:var(--muted);padding:1.5px 0}
.footer-bar{position:absolute;top:1176px;left:0;width:692px;height:24px;background:var(--footer-bar);color:#bbb;font-size:5.8px;display:flex;justify-content:space-between;align-items:center;padding:0 54px}
.footer-bar nav{display:flex;gap:8px}
</style>
</head>
<body>
<div class="topbar">
  <span>+1 (555) 010 4477 &nbsp;|&nbsp; hello@fenderpals-example.com</span>
  <div class="social"><span></span><span></span><span></span><span></span></div>
</div>
<header class="header">
  <div class="brand">FENDERPALS</div>
  <nav class="nav">
    <a>Home</a><a>About Us</a><a class="active">Expertise</a><a>World Done</a><a>Resources</a><a>News</a><a>Contact</a><span class="badge"></span>
  </nav>
</header>

<section class="hero">
  <h1>We focus Only on Car Wrecks</h1>
  <div class="hero-body">
    <div class="hero-copy">
      <p>We have a lot of experience and expertise in the section of Car Wrecks as we worked for a wide number of years only on this section. And now it's easy to speak about us that we are the number one Group on this section. Lorem ipsum dolor sit amet, consectetur adipiscing elit, sed do eiusmod tempor incididunt ut et dolore magna aliqua. Lorem ipsum dolor sit amet, consectetur adipiscing elit, sed do eiusmod tempor incididunt ut et dolore magna aliqua.</p>
      <ul class="checklist">
        <li><svg width="7" height="7" viewBox="0 0 10 10"><path d="M1 5l3 3 5-6" stroke="#ec1f27" stroke-width="2" fill="none"/></svg>Lorem ipsum dolor sit amet, consectetur adipiscing elit</li>
        <li><svg width="7" height="7" viewBox="0 0 10 10"><path d="M1 5l3 3 5-6" stroke="#ec1f27" stroke-width="2" fill="none"/></svg>Lorem ipsum dolor sit amet, consectetur adipiscing elit</li>
        <li><svg width="7" height="7" viewBox="0 0 10 10"><path d="M1 5l3 3 5-6" stroke="#ec1f27" stroke-width="2" fill="none"/></svg>Lorem ipsum dolor sit amet, consectetur adipiscing elit</li>
        <li><svg width="7" height="7" viewBox="0 0 10 10"><path d="M1 5l3 3 5-6" stroke="#ec1f27" stroke-width="2" fill="none"/></svg>Lorem ipsum dolor sit amet, consectetur adipiscing elit</li>
        <li><svg width="7" height="7" viewBox="0 0 10 10"><path d="M1 5l3 3 5-6" stroke="#ec1f27" stroke-width="2" fill="none"/></svg>Lorem ipsum dolor sit amet, consectetur adipiscing elit</li>
        <li><svg width="7" height="7" viewBox="0 0 10 10"><path d="M1 5l3 3 5-6" stroke="#ec1f27" stroke-width="2" fill="none"/></svg>Lorem ipsum dolor sit amet, consectetur adipiscing elit</li>
        <li><svg width="7" height="7" viewBox="0 0 10 10"><path d="M1 5l3 3 5-6" stroke="#ec1f27" stroke-width="2" fill="none"/></svg>Lorem ipsum dolor sit amet, consectetur adipiscing elit</li>
        <li><svg width="7" height="7" viewBox="0 0 10 10"><path d="M1 5l3 3 5-6" stroke="#ec1f27" stroke-width="2" fill="none"/></svg>Lorem ipsum dolor sit amet, consectetur adipiscing elit</li>
      </ul>
    </div>
    <div class="hero-photo" role="img" aria-label="Photo of a damaged blue car after a wreck"></div>
  </div>
</section>

<section class="aspects">
  <h2>The different aspects including in our<br>Service/Expertise on this section are:</h2>
  <div class="aspect-row">
    <div class="aspect">
      <svg width="22" height="22" viewBox="0 0 22 22"><path d="M6 2v14h14M2 6h14v14" stroke="#ec1f27" stroke-width="2.5" fill="none"/></svg>
      <div><h3>Damages</h3><p>Lorem ipsum dolor sit amet, consectetur adipiscing elit</p></div>
    </div>
    <div class="aspect">
      <svg width="22" height="22" viewBox="0 0 22 22"><circle cx="9" cy="7" r="4" fill="#ec1f27"/><path d="M2 19c0-5 3-7 7-7s7 2 7 7z" fill="#ec1f27"/><path d="M18 8v8M14 12h8" stroke="#ec1f27" stroke-width="2.5"/></svg>
      <div><h3>Insurance</h3><p>Lorem ipsum dolor sit amet, consectetur adipiscing elit</p></div>
    </div>
    <div class="aspect">
      <svg width="22" height="22" viewBox="0 0 22 22"><circle cx="11" cy="12" r="6" fill="#ec1f27"/><path d="M11 2v4M3 5l3 3M19 5l-3 3M3 19h16" stroke="#ec1f27" stroke-width="2"/></svg>
      <div><h3>Investigation</h3><p>Lorem ipsum dolor sit amet, consectetur adipiscing elit</p></div>
    </div>
  </div>
</section>

<section class="cta">
  <h2>Ready to get started</h2>
  <p>Lorem ipsum dolor sit amet, consectetur adipiscing elit, sed do eiusmod tempor incididunt ut labore et dolore magna aliqua. Ut enim ad minim veniam, quis nostrud exercitation ullamco laboris nisi ut aliquip ex ea commodo.</p>
  <span class="btn">Request a Free Quote</span>
</section>

<section class="reviews">
  <h2>What Clients say about our Expertise on Car Wrecks</h2>
  <p class="intro">Lorem ipsum dolor sit amet, consectetur adipiscing elit, sed do eiusmod tempor incididunt ut labore et dolore magna aliqua. Ut enim ad minim veniam.</p>
  <div class="review-row">
    <div class="review">
      <div class="avatar" role="img" aria-label="Portrait of a client"></div>
      <p>Lorem ipsum dolor sit amet, consectetur adipiscing elit, sed do eiusmod tempor incididunt ut labore.</p>
      <cite>John Doe / Director of Example Co.</cite>
    </div>
    <div class="review">
      <div class="avatar" role="img" aria-label="Portrait of a client"></div>
      <p>Lorem ipsum dolor sit amet, consectetur adipiscing elit, sed do eiusmod tempor incididunt ut labore.</p>
      <cite>John Doe / Director of Example Co.</cite>
    </div>
    <div class="review">
      <div class="avatar" role="img" aria-label="Portrait of a client"></div>
      <p>Lorem ipsum dolor sit amet, consectetur adipiscing elit, sed do eiusmod tempor incididunt ut labore.</p>
      <cite>John Doe / Director of Example Co.</cite>
    </div>
  </div>
</section>

<footer class="footer">
  <div class="col"><h4>COMPANY</h4><ul><li>About us</li><li>Meet the team</li><li>Careers</li><li>Our history</li><li>Contact us</li></ul></div>
  <div class="col"><h4>SUPPORT</h4><ul><li>FAQ</li><li>Blog</li><li>Forum</li><li>Guides</li><li>Help center</li><li>Billing</li></ul></div>
  <div class="col"><h4>NECESSARY LINKS</h4><ul><li>Lorem ipsum dolor</li><li>Lorem ipsum dolor</li><li>Lorem ipsum dolor</li><li>Lorem ipsum dolor</li><li>Lorem ipsum dolor</li></ul></div>
  <div class="col"><h4>VALUED PARTNERS</h4><ul><li>Partner one</li><li>Partner two</li><li>Partner three</li><li>Partner four</li><li>Partner five</li></ul></div>
</footer>
<div class="footer-bar">
  <span>© 2024 FenderPals. All Rights Reserved.</span>
  <nav><span>Home</span><span>About Us</span><span>Help</span><span>Contact</span></nav>
</div>
</body>
</html>
```